I would like a single page website for Kestrel Lift Rentals. In the file list provided there is basic information to be included as well as our logo with colors, fonts and images to be included.
Site must be very simple and be able to be loaded onto smart phones etc very quickly.
Site needs to be very smart in appearance

Target Market(s)

All prospective drone customers from Police to Parties.

Industry/Entity Type

Hire

Coding

Coded - Design and coding required

Number of Pages Required

1 page

Requirements
Must have
• Must have variation of color schemes supplied
Nice to have
• Must be very eye catching without going over the top
Should not have
• Anything slow to load.

```html
<!DOCTYPE html>
<html lang="en">
<head>
<meta charset="utf-8">
<title>Kestrel Lift Rentals</title>
<link rel="stylesheet" href="https://fonts.googleapis.com/css2?family=Barlow:wght@500;600;700&family=Roboto:wght@400;500&display=swap">
<style>
:root{
  --green:#8dc63f;
  --green-deep:#6aaa1e;
  --green-text:#62a51a;
  --ink:#2b2b2b;
  --body:#444;
  --muted:#777;
  --white:#fff;
  --dark:#1a1a1a;
  --darker:#151515;
  --social-blue:#2e4690;
  --btn:#2c2c2c;
}
*{margin:0;padding:0;box-sizing:border-box}
html,body{width:1200px;height:2590px;overflow:hidden}
body{position:relative;background:var(--white);font-family:"Roboto",Arial,sans-serif;color:var(--body)}
.abs{position:absolute}
.topbar{left:0;top:0;width:1200px;height:35px;background:var(--green);color:var(--white);font-size:14px}
.topbar .welcome{left:92px;top:9px}
.topbar .call{right:92px;top:9px}
.header{left:0;top:35px;width:1200px;height:138px;background:var(--white)}
.brand{left:86px;top:34px;display:flex;align-items:center;gap:12px}
.brand-mark{width:24px;height:24px;border-radius:50%;background:var(--green-deep)}
.brand-name{font-family:"Barlow",Arial,sans-serif;font-weight:700;font-size:30px;color:var(--green-deep);line-height:32px}
.nav{right:92px;top:62px;display:flex;gap:48px;font-size:15.5px;font-family:"Roboto",Arial,sans-serif;color:var(--ink)}
.nav .active{color:var(--green)}
.hero{left:0;top:173px;width:1200px;height:587px;background:linear-gradient(180deg,#4d4540 0%,#3a3f48 35%,#2b3038 70%,#1d2228 100%)}
.hero-drone{left:500px;top:80px;width:580px;height:350px;border-radius:40px;background:radial-gradient(ellipse at center,#d9d9d9 0%,#a9a9a9 45%,rgba(80,80,80,0) 72%)}
.hero-title{left:94px;top:220px;font-family:"Barlow",Arial,sans-serif;font-weight:700;font-size:50px;line-height:64px;color:var(--white);letter-spacing:1px}
.hero-title span{color:var(--green)}
.hero-arrows{left:95px;top:367px;width:97px;height:57px;background:rgba(0,0,0,.75);display:flex}
.hero-arrows svg{width:48px;height:57px}
.hero-shadow{left:200px;top:760px;width:800px;height:24px;background:radial-gradient(ellipse at top,rgba(0,0,0,.22),rgba(0,0,0,0) 70%)}
.section-title{font-family:"Barlow",Arial,sans-serif;font-weight:600;font-size:30px;color:var(--ink);letter-spacing:.5px}
.section-title span{color:var(--green-text)}
.welcome-title{left:0;top:816px;width:1200px;text-align:center}
.welcome-copy{left:92px;top:870px;width:987px;text-align:center;font-size:14.5px;line-height:29px;color:var(--body)}
.services-title{left:92px;top:1028px;font-size:25px}
.services-arrows{left:1034px;top:1034px;display:flex;gap:3px}
.services-arrows svg{width:21px;height:21px}
.card{top:1079px;width:236px}
.card-photo{width:236px;height:155px;border:4px solid #eee;box-shadow:0 1px 4px rgba(0,0,0,.35)}
.card-title{margin-top:20px;font-family:"Barlow",Arial,sans-serif;font-weight:600;font-size:16px;color:var(--green-text)}
.card-copy{margin-top:10px;font-size:12.5px;line-height:18px;color:var(--muted);text-align:justify;hyphens:auto;-webkit-hyphens:auto}
.card-btn{display:inline-block;margin-top:18px;width:94px;height:33px;line-height:33px;text-align:center;background:var(--btn);color:var(--white);font-size:11.5px;border-radius:3px}
.video-band{left:0;top:1443px;width:1200px;height:404px;background:linear-gradient(180deg,#b9c9d8 0%,#dbe3ea 50%,#7e9a57 80%,#5f7d3a 100%)}
.play{left:549px;top:1610px;width:84px;height:84px}
.points-title{left:0;top:1898px;width:1200px;text-align:center;font-size:28px}
.points-photo{left:86px;top:1963px;width:275px;height:204px;border:4px solid #eee;box-shadow:0 1px 5px rgba(0,0,0,.35);background:radial-gradient(ellipse at 50% 55%,#e7e7e7 0%,#a38a45 35%,#6d5a29 100%)}
.points-list{list-style:none;font-size:14.5px;color:var(--body)}
.points-list li{height:36.5px;display:flex;align-items:center;gap:9px}
.points-list svg{width:14px;height:14px;flex:none}
.footer{left:0;top:2213px;width:1200px;height:180px;background:var(--green-deep);color:var(--white)}
.footer-col{top:25px}
.footer-col h4{font-weight:400;font-size:15.5px;padding-bottom:8px;border-bottom:1px solid rgba(255,255,255,.35);width:max-content;padding-right:20px}
.footer-col ul{list-style:none;margin-top:9px;font-size:11px;line-height:22.5px}
.social{left:0;top:2393px;width:1200px;height:104px;background:var(--dark)}
.social-item{top:0;height:104px;line-height:104px;text-align:center;color:var(--white);font-family:"Barlow",Arial,sans-serif;font-weight:600;font-size:24px}
.social-item.highlight{background:var(--social-blue)}
.copyright{left:0;top:2497px;width:1200px;height:93px;background:var(--darker);color:var(--white);text-align:center;font-size:13.5px;line-height:86px}
</style>
</head>
<body>

<div class="abs topbar">
  <span class="abs welcome">Welcome to Kestrel Lift Rentals</span>
  <span class="abs call">CALL NOW : 0400 555 123</span>
</div>

<header class="abs header">
  <div class="abs brand">
    <span class="brand-mark"></span>
    <span class="brand-name">KESTREL LIFT<br>RENTALS</span>
  </div>
  <nav class="abs nav">
    <span class="active">HOME</span>
    <span>DRONE SERVICES</span>
    <span>ABOUT</span>
    <span>CONTACT</span>
    <span>LOGIN</span>
  </nav>
</header>

<section class="abs hero" role="img" aria-label="White camera drone hovering over a blurred city skyline at dusk">
  <div class="abs hero-drone"></div>
  <h1 class="abs hero-title">DRONE <span>PHOTOGRAPHY</span><br>&amp; VIDEO SERVICES</h1>
  <div class="abs hero-arrows">
    <svg viewBox="0 0 48 57"><path d="M29 17 L19 28.5 L29 40" fill="none" stroke="#fff" stroke-width="2"/></svg>
    <svg viewBox="0 0 48 57"><path d="M19 17 L29 28.5 L19 40" fill="none" stroke="#fff" stroke-width="2"/></svg>
  </div>
</section>
<div class="abs hero-shadow"></div>

<h2 class="abs section-title welcome-title">WELCOME TO <span>KESTREL LIFT RENTALS</span></h2>
<p class="abs welcome-copy">Lorem Ipsum has been the industry's standard dummy text ever since the 1500s, when an unknown printer took a galley of type and scrambled it to make a type specimen book. It has survived not only five centuries, but also the leap into electronic typesetting, remaining essentially unchanged. It was popularised in the 1960s with the release of Lettrovane sheets containing Lorem Ipsum passages, and more recently with desktop publishing</p>

<h2 class="abs section-title services-title">DRONE <span>SERVICES</span></h2>
<div class="abs services-arrows">
  <svg viewBox="0 0 21 21"><rect width="21" height="21" fill="#111"/><path d="M12.5 6 L8 10.5 L12.5 15" fill="none" stroke="#fff" stroke-width="1.5"/></svg>
  <svg viewBox="0 0 21 21"><rect width="21" height="21" fill="#111"/><path d="M8.5 6 L13 10.5 L8.5 15" fill="none" stroke="#fff" stroke-width="1.5"/></svg>
</div>

<article class="abs card" style="left:90px">
  <div class="card-photo" role="img" aria-label="Children celebrating at a birthday party table" style="background:linear-gradient(160deg,#3f7d3a,#c23a2e 60%,#d9462f)"></div>
  <h3 class="card-title">HIRE FOR PARTIES</h3>
  <p class="card-copy">Lorem Ipsum has been the industry's standard dummy text ever since the 1500s, when an unknown printer</p>
  <span class="card-btn">READ MORE</span>
</article>
<article class="abs card" style="left:344px">
  <div class="card-photo" role="img" aria-label="Security cameras mounted on a glass office tower" style="background:linear-gradient(160deg,#cfd8e0,#4f86b8 55%,#2d5f92)"></div>
  <h3 class="card-title">SURVEILLANCE</h3>
  <p class="card-copy">Lorem Ipsum has been the industry's standard dummy text ever since the 1500s, when an unknown printer</p>
  <span class="card-btn">READ MORE</span>
</article>
<article class="abs card" style="left:596px">
  <div class="card-photo" role="img" aria-label="Two football players competing for the ball" style="background:linear-gradient(160deg,#5b6066,#a6a9ab 50%,#3f4347)"></div>
  <h3 class="card-title">SPORTING EVENTS</h3>
  <p class="card-copy">Lorem Ipsum has been the industry's standard dummy text ever since the 1500s, when an unknown printer</p>
  <span class="card-btn">READ MORE</span>
</article>
<article class="abs card" style="left:848px">
  <div class="card-photo" role="img" aria-label="Construction worker in a hard hat beside a yellow crane" style="background:linear-gradient(160deg,#e7d34a,#d8bf3c 45%,#c8392b)"></div>
  <h3 class="card-title">CONSTRUCTION PROJECT</h3>
  <p class="card-copy">Lorem Ipsum has been the industry's standard dummy text ever since the 1500s, when an unknown printer</p>
  <span class="card-btn">READ MORE</span>
</article>

<section class="abs video-band" role="img" aria-label="Film crew operating a camera drone over a green field, video preview"></section>
<svg class="abs play" viewBox="0 0 84 84" aria-label="Play video">
  <circle cx="42" cy="42" r="42" fill="rgba(40,40,40,.75)"/>
  <path d="M33 25 L61 42 L33 59 Z" fill="#fff"/>
</svg>

<h2 class="abs section-title points-title">DRONES <span>POINTS</span></h2>
<div class="abs points-photo" role="img" aria-label="White drone flying over a blurred autumn background"></div>

<ul class="abs points-list" style="left:383px;top:1968px">
  <li><svg viewBox="0 0 14 14"><circle cx="7" cy="7" r="6" fill="none" stroke="#62a51a" stroke-width="1.5"/><path d="M5.5 4.5 L8.5 7 L5.5 9.5" fill="#62a51a"/></svg>Special Occasions, Children's Birthday Parties, Weddings</li>
  <li><svg viewBox="0 0 14 14"><circle cx="7" cy="7" r="6" fill="none" stroke="#62a51a" stroke-width="1.5"/><path d="M5.5 4.5 L8.5 7 L5.5 9.5" fill="#62a51a"/></svg>Sporting events –4K&nbsp; Video of yourself participating in marathons</li>
  <li><svg viewBox="0 0 14 14"><circle cx="7" cy="7" r="6" fill="none" stroke="#62a51a" stroke-width="1.5"/><path d="M5.5 4.5 L8.5 7 L5.5 9.5" fill="#62a51a"/></svg>Real Estate Brochures</li>
  <li><svg viewBox="0 0 14 14"><circle cx="7" cy="7" r="6" fill="none" stroke="#62a51a" stroke-width="1.5"/><path d="M5.5 4.5 L8.5 7 L5.5 9.5" fill="#62a51a"/></svg>Construction project updates for remote stake holders</li>
  <li><svg viewBox="0 0 14 14"><circle cx="7" cy="7" r="6" fill="none" stroke="#62a51a" stroke-width="1.5"/><path d="M5.5 4.5 L8.5 7 L5.5 9.5" fill="#62a51a"/></svg>Surveillance – Police, Local councils worksafe etc</li>
</ul>
<ul class="abs points-list" style="left:846px;top:1968px">
  <li><svg viewBox="0 0 14 14"><circle cx="7" cy="7" r="6" fill="none" stroke="#62a51a" stroke-width="1.5"/><path d="M5.5 4.5 L8.5 7 L5.5 9.5" fill="#62a51a"/></svg>Building/Roof Condition Inspections</li>
  <li><svg viewBox="0 0 14 14"><circle cx="7" cy="7" r="6" fill="none" stroke="#62a51a" stroke-width="1.5"/><path d="M5.5 4.5 L8.5 7 L5.5 9.5" fill="#62a51a"/></svg>Lost pets</li>
  <li><svg viewBox="0 0 14 14"><circle cx="7" cy="7" r="6" fill="none" stroke="#62a51a" stroke-width="1.5"/><path d="M5.5 4.5 L8.5 7 L5.5 9.5" fill="#62a51a"/></svg>Accident reconstructions</li>
  <li><svg viewBox="0 0 14 14"><circle cx="7" cy="7" r="6" fill="none" stroke="#62a51a" stroke-width="1.5"/><path d="M5.5 4.5 L8.5 7 L5.5 9.5" fill="#62a51a"/></svg>Insurance assessing</li>
</ul>

<footer class="abs footer">
  <div class="abs footer-col" style="left:92px"><h4>About Us</h4><ul><li>History</li><li>Board</li><li>National Coverage</li><li>Quality Management System</li></ul></div>
  <div class="abs footer-col" style="left:314px"><h4>Training Classes</h4><ul><li>Strategy and Architecture</li><li>Program and Project Management</li><li>Business Analysis</li><li>Application Development</li></ul></div>
  <div class="abs footer-col" style="left:589px"><h4>Experience</h4><ul><li>Excellence Together</li><li>The Recruitment Process</li><li>Graduates</li><li>Apply</li></ul></div>
  <div class="abs footer-col" style="left:801px"><h4>Projects</h4><ul><li>Share Price</li><li>Financial Reports</li><li>Exchange Announcements</li><li>Corporate Governance</li></ul></div>
  <div class="abs footer-col" style="left:1000px"><h4>Other</h4><ul><li>Contact</li><li>Privacy</li><li>Environment</li><li>Diversity</li></ul></div>
</footer>

<nav class="abs social">
  <span class="abs social-item highlight" style="left:0;width:364px">Chatterly</span>
  <span class="abs social-item" style="left:366px;width:200px">Tweetline</span>
  <span class="abs social-item" style="left:627px;width:220px">Pinboardia</span>
  <span class="abs social-item" style="left:844px;width:180px">Shotbox</span>
</nav>

<div class="abs copyright">Copyright &nbsp;© 2015 All Rights Reserved,</div>

</body>
</html>
```